Business card for a young aspring actress

My daughter is 18 and just starting out on her profession as an actress. She is a member of the Harbour Young Players and has already had some extras work and a featured role in an upcoming Feature film.

She wants/needs a card that she can have to hand to give to those she comes into contact with in the theatre, TV and film industries.

We are thinking that it may be double sided with an impact side including a picture of her and her name etc with the reverse holding contact and other details.

She wants to go by the name Maya Louise Brennick.

She has done a little modelling but sees herself as an actress.

She can be seen in this video
http://www.oakvalepark-academy.org/videos/be0881e4276ee2512c50a07f907c1d03?width=640&height=480

Target Market(s)

Anyone she comes into contact with in theatre TV and film industries.

Industry/Entity Type

Business

Requirements
Nice to have
• She has email and a website www.mayabrennick.com She is quite a connected girl

```html
<!DOCTYPE html>
<html lang="en">
<head>
<meta charset="utf-8">
<title>Maya Louise Brennick – Actress Business Card</title>
<link rel="stylesheet" href="https://fonts.googleapis.com/css2?family=Great+Vibes&family=Cormorant+SC:wght@500&family=Cormorant+Garamond:wght@500&display=swap">
<style>
  :root {
    --backdrop: #e4e2df;
    --card: #ffffff;
    --ink: #1a1a1a;
    --bar: #8a8a8a;
    --bar-edge: #2b2b2b;
    --frame: #151515;
    --sketch-light: #f4f4f4;
    --sketch-dark: #c4c4c4;
    --photo-a: #6f7a5a;
    --photo-b: #c9b7a4;
    --caption: #d8d8d8;
  }
  * { margin: 0; padding: 0; box-sizing: border-box; }
  html, body { width: 1200px; height: 900px; overflow: hidden; }
  body {
    background: var(--backdrop);
    display: flex;
    flex-direction: column;
    align-items: center;
    justify-content: center;
    gap: 60px;
    color: var(--ink);
  }
  .card {
    position: relative;
    width: 630px;
    height: 360px;
    background: var(--card);
    box-shadow: 0 8px 24px rgba(0,0,0,.18);
    overflow: hidden;
  }

  /* Front */
  .portrait-sketch {
    position: absolute;
    left: 0; top: 0;
    width: 290px; height: 290px;
    background: radial-gradient(circle at 50% 45%, var(--sketch-light) 30%, var(--sketch-dark) 60%, var(--card) 71%);
  }
  .front-title {
    position: absolute;
    left: 300px; right: 20px; top: 185px;
    text-align: center;
  }
  .front-name {
    font-family: "Great Vibes", cursive;
    font-size: 38px;
    line-height: 1.1;
    white-space: nowrap;
  }
  .front-role {
    font-family: "Cormorant SC", serif;
    font-size: 28px;
    letter-spacing: 1px;
    margin-top: 8px;
  }

  /* Back */
  .back-name {
    position: absolute;
    right: 40px; top: 26px;
    font-family: "Cormorant SC", serif;
    font-weight: 500;
    font-size: 32px;
    letter-spacing: 1px;
    white-space: nowrap;
  }
  .divider {
    position: absolute;
    left: 0; top: 78px;
    width: 100%; height: 9px;
    background: var(--bar);
    border-top: 2px solid var(--bar-edge);
    border-bottom: 2px solid var(--bar-edge);
  }
  .polaroids { position: absolute; left: 26px; top: 116px; width: 340px; height: 220px; }
  .polaroid {
    position: absolute;
    background: var(--frame);
    padding: 12px 12px 30px;
  }
  .polaroid--back { left: 0; top: 0; width: 200px; height: 165px; transform: rotate(-8deg); }
  .polaroid--front { left: 160px; top: 45px; width: 170px; height: 150px; transform: rotate(10deg); }
  .photo { width: 100%; height: 100%; }
  .polaroid--back .photo { background: linear-gradient(135deg, var(--photo-a), var(--photo-b)); }
  .polaroid--front .photo { background: linear-gradient(160deg, var(--photo-b), #8d7d70); }
  .polaroid-caption {
    position: absolute;
    bottom: 6px;
    font-family: "Great Vibes", cursive;
    font-size: 13px;
    color: var(--caption);
    white-space: nowrap;
  }
  .polaroid--back .polaroid-caption { left: 14px; }
  .polaroid--front .polaroid-caption { right: 14px; }
  .contact {
    position: absolute;
    left: 392px; top: 150px;
    list-style: none;
    font-family: "Cormorant Garamond", serif;
    font-size: 17px;
    line-height: 1.5;
    white-space: nowrap;
  }
</style>
</head>
<body>
  <section class="card card--front">
    <div class="portrait-sketch" role="img" aria-label="Pencil sketch portrait of Maya Louise Brennick"></div>
    <div class="front-title">
      <p class="front-name">Maya Louise Brennick.</p>
      <p class="front-role">Actress</p>
    </div>
  </section>

  <section class="card card--back">
    <h1 class="back-name">Maya Louise Brennick.</h1>
    <div class="divider"></div>
    <div class="polaroids">
      <figure class="polaroid polaroid--back">
        <div class="photo" role="img" aria-label="Headshot photograph of Maya"></div>
        <figcaption class="polaroid-caption">Maya Louise Brennick</figcaption>
      </figure>
      <figure class="polaroid polaroid--front">
        <div class="photo" role="img" aria-label="Casual photograph of Maya smiling"></div>
        <figcaption class="polaroid-caption">Brennick</figcaption>
      </figure>
    </div>
    <ul class="contact">
      <li>Tel: 07700 900456</li>
      <li>Email: hello@mayabrennick.com</li>
      <li>Web: www.mayabrennick.com</li>
    </ul>
  </section>
</body>
</html>
```